Presentation Folder

Design presentation folder for professional law firm. Our law firm primarily represents individuals who are dealing with divorce, child custody, child support, spousal support, wills, estates and other civil litigation.
We desire a simple, professional, but memorable presentation folder that we can give clients containing their important documents (e.g., contract, and other important papers). The folder will also have a place for a business card. We will print this at Prindlebay. Specs and Templates are available at http://www.prindlebay-example.com/vp/ns/propath/UploadResources.aspx?selectedTab=0?pfid=156&pf_id=156&xnav=studio-side-bar#Templates
Our logo and one of our business cards is attached.
Our website is www.HolloweyFamilyLaw-example.com
Target Market(s)
Individual with legal issues primarily undergoing divorce
Industry/Entity Type
Law Firm
Font styles to use
Other font styles liked:
- Tahoma
Look and feel

```html
<!DOCTYPE html>
<html lang="en">
<head>
<meta charset="utf-8">
<title>Hollowey Law – Presentation Folder</title>
<link rel="stylesheet" href="https://fonts.googleapis.com/css2?family=Tinos:wght@400;700&display=swap">
<style>
  :root {
    --paper: #ffffff;
    --navy: #262a5e;
    --navy-deep: #1e2150;
    --navy-light: #3a4180;
    --gold-text: #c0a468;
    --cream: #f3ecd8;
  }
  html, body {
    margin: 0;
    padding: 0;
    width: 1200px;
    height: 848px;
    overflow: hidden;
    background: var(--paper);
  }
  .folder-canvas {
    display: block;
    width: 1200px;
    height: 848px;
  }
  .folder-text {
    font-family: "Tinos", "Times New Roman", serif;
    fill: var(--gold-text);
  }
  .tagline { font-size: 8.6px; }
  .firm-name { font-size: 9px; }
  .contact-line { font-size: 5.8px; }
  .mark-name {
    font-family: "Tinos", "Times New Roman", serif;
    font-weight: 700;
    fill: var(--navy);
  }
  .card-text {
    font-family: "Tinos", "Times New Roman", serif;
    fill: var(--gold-text);
    font-size: 5.2px;
  }
</style>
</head>
<body>
<svg class="folder-canvas" viewBox="0 0 1200 848" xmlns="http://www.w3.org/2000/svg">
  <defs>
    <radialGradient id="cover-glow" cx="0.25" cy="0.5" r="0.6">
      <stop offset="0" stop-color="#8a7a4a"/>
      <stop offset="0.35" stop-color="#3a3f78"/>
      <stop offset="1" stop-color="#262a5e" stop-opacity="0"/>
    </radialGradient>
  </defs>

  <!-- folder die shape -->
  <path class="folder-shape" fill="var(--navy)"
    d="M86 10 H1104 V388 A14 14 0 0 0 1104 416 V612 H1086 V836
       H662 Q646 836 644 820 L620 622 Q618 612 612 612 Q606 612 606 622
       L626 820 Q626 836 612 836 H128 V612 H86 V402 A14 14 0 0 0 86 374 Z"/>

  <!-- front cover decorative area -->
  <rect class="cover-glow" x="606" y="250" width="480" height="362"
        fill="url(#cover-glow)" role="img"
        aria-label="Soft gold and navy decorative glow on the front cover"/>

  <!-- front cover name mark -->
  <g class="front-mark">
    <rect x="972" y="48" width="80" height="82" fill="var(--cream)"/>
    <text class="mark-name" x="1012" y="86" font-size="11" text-anchor="middle">HOLLOWEY</text>
    <text class="mark-name" x="1012" y="101" font-size="11" text-anchor="middle">LAW</text>
  </g>

  <!-- back cover -->
  <g class="back-cover folder-text" text-anchor="middle">
    <text class="tagline" x="368" y="306">Hollowey Law provides full-service representation of clients in New Hanover,</text>
    <text class="tagline" x="368" y="317">Pender, Brunswick, and Moore counties plus unbundled online legal services</text>
    <text class="tagline" x="368" y="328">throughout the State of North Carolina.</text>
    <rect x="352" y="504" width="27" height="28" fill="var(--cream)"/>
    <text class="firm-name" x="366" y="550">Hollowey Law, PLLC</text>
    <text class="contact-line" x="366" y="560">210 Harbor Lane, Suite 4 | PO Box 417 | Seabrook, NC 28400</text>
    <text class="contact-line" x="366" y="572">Telephone: (910) 555-0142 | Facsimile: (910) 555-0187 | Email: info@holloweyfamilylaw-example.com</text>
  </g>

  <!-- business card slot, printed upside down on the pocket -->
  <g class="card-slot" transform="rotate(180 364 723)">
    <rect x="314" y="636" width="100" height="175" fill="var(--navy-light)" opacity="0.3"/>
    <rect x="331" y="648" width="66" height="62" fill="var(--cream)"/>
    <text class="mark-name" x="364" y="683" font-size="8" text-anchor="middle">HOLLOWEY</text>
    <g class="card-text" text-anchor="middle">
      <text x="364" y="734" font-size="6">MORGAN ELLIS HOLLOWEY</text>
      <text x="364" y="742">Attorney at Law</text>
      <text x="364" y="754">210 Harbor Lane, Suite 4</text>
      <text x="364" y="761">Seabrook, NC 28400</text>
      <text x="364" y="772">T: (910) 555-0142</text>
      <text x="364" y="780">E: mhollowey@holloweyfamilylaw-example.com</text>
    </g>
  </g>
</svg>
</body>
</html>
```